Austrian finance und insurance broker needs business card design

We Need a serious looking Design for Business Card. we consult private and corporates customers in finance and insurance questions. the final design should express security and experience. We consult customers in questions of loans, Investments and insurance and have a wide range of Banks to offer. We compare several offers and select the best for our customers.

Target Market(s)

private and coporate customers with efforts in Money and insurance

Industry/Entity Type

Insurance Broker

Contact Information for Business Card

Bernhard Aigner
Geschäftsführer
staatl. geprüfter Vermögensberater und Versicherungsmakler
Tel: 0664 521 8409
office@der-brandl.at
www.der-brandl.at
Leopold Hainz Gasse 14
2183 Melkstetten
GISA Nr. 48270315 u. 51736048 (backside)

Font styles to use
Serif
Sans Serif

Requirements
Must have
• logo (designcrowd zip) and all Details
Nice to have
• makler logo design, maybe a 2 coloured Version is possible

```html
<!DOCTYPE html>
<html lang="de">
<head>
<meta charset="utf-8">
<title>Aigner Finanzberatung – Visitenkarte</title>
<link href="https://fonts.googleapis.com/css2?family=Nunito:wght@600;700;800&family=Roboto+Condensed:wght@400&display=swap" rel="stylesheet">
<style>
  :root {
    --stage: #c9c9c9;
    --brand-blue: #0a56a0;
    --brand-blue-dark: #074a8c;
    --card-light: #f4f4f4;
    --card-light-edge: #e6e6e6;
    --ink: #2f2f2f;
    --ink-soft: #444;
    --rule-gray: #5c5c5c;
    --band-gray: #5e6062;
    --seal-red: #b3141b;
    --white: #ffffff;
  }
  * { box-sizing: border-box; margin: 0; padding: 0; }
  html, body { width: 1200px; height: 576px; overflow: hidden; }
  body { background: var(--stage); position: relative; font-family: "Nunito", sans-serif; }

  .card {
    position: absolute;
    border-radius: 12px;
    overflow: hidden;
    box-shadow: 0 3px 8px rgba(0,0,0,0.25);
  }

  /* Back side */
  .card-back {
    left: 82px; top: 139px; width: 484px; height: 293px;
    background: linear-gradient(180deg, #0b5aa6 0%, var(--brand-blue-dark) 100%);
    color: var(--white);
  }
  .card-back .brand-mark {
    position: absolute; left: 86px; top: 101px;
    width: 72px; height: 72px; border-radius: 50%;
    background: var(--white);
  }
  .card-back .brand-divider {
    position: absolute; left: 176px; top: 91px; width: 2px; height: 92px;
    background: var(--white);
  }
  .card-back .brand-name {
    position: absolute; left: 186px; top: 112px;
    font-size: 16px; font-weight: 700; white-space: nowrap;
  }
  .card-back .brand-tagline {
    position: absolute; left: 186px; top: 136px;
    font-size: 13px; font-weight: 700; white-space: nowrap;
  }
  .card-back .gisa {
    position: absolute; left: 0; right: 0; top: 262px;
    text-align: center; font-size: 12.5px; font-weight: 600; letter-spacing: 0.2px;
  }

  /* Front side */
  .card-front {
    left: 602px; top: 138px; width: 481px; height: 291px;
    background: linear-gradient(160deg, var(--white) 0%, var(--card-light) 55%, var(--card-light-edge) 100%);
    color: var(--ink);
  }
  .card-front .brand-mark {
    position: absolute; left: 22px; top: 32px;
    width: 56px; height: 56px; border-radius: 50%;
    background: var(--brand-blue);
  }
  .card-front .brand-divider {
    position: absolute; left: 97px; top: 26px; width: 1.5px; height: 68px;
    background: var(--rule-gray);
  }
  .card-front .brand-name {
    position: absolute; left: 104px; top: 43px;
    font-size: 14px; font-weight: 700; color: var(--brand-blue); white-space: nowrap;
  }
  .card-front .brand-tagline {
    position: absolute; left: 104px; top: 63px;
    font-size: 11px; font-weight: 700; color: var(--ink-soft); white-space: nowrap;
  }
  .portrait {
    position: absolute; left: 330px; top: 14px; width: 151px; height: 168px;
    background: linear-gradient(180deg, #e9e9e9 0%, #c7a58e 45%, #2d2f3a 100%);
  }
  .person-name {
    position: absolute; left: 20px; top: 119px;
    font-size: 21px; font-weight: 800; color: var(--brand-blue); white-space: nowrap;
  }
  .person-role, .person-title {
    position: absolute; left: 20px;
    font-family: "Roboto Condensed", sans-serif; font-size: 11.5px; color: var(--ink-soft); white-space: nowrap;
  }
  .person-role { top: 146px; }
  .person-title { top: 162px; }
  .name-rule {
    position: absolute; left: 20px; right: 0; top: 182px; height: 2px;
    background: var(--brand-blue);
  }
  .contact-list {
    position: absolute; left: 22px; top: 200px; list-style: none;
    font-family: "Roboto Condensed", sans-serif; font-size: 12.5px; color: var(--ink);
  }
  .contact-list li { display: flex; align-items: center; height: 16.5px; }
  .contact-list svg { width: 11px; height: 11px; margin-right: 12px; fill: var(--ink); }
  .address {
    position: absolute; left: 22px; top: 251px;
    font-family: "Roboto Condensed", sans-serif; font-size: 12.5px; color: var(--ink); white-space: nowrap;
  }
  .partner-badge {
    position: absolute; left: 279px; top: 205px; width: 38px; height: 38px; border-radius: 50%;
    background: radial-gradient(circle at 40% 35%, #d2262d 0%, var(--seal-red) 60%, #7e0c10 100%);
  }
  .band-gray {
    position: absolute; left: 0; right: 0; bottom: 0; height: 12px; background: var(--band-gray);
  }
  .band-blue { position: absolute; left: 228px; bottom: 0; width: 253px; height: 32px; }
  .band-blue .gisa {
    position: absolute; left: 52px; top: 9px;
    font-family: "Roboto Condensed", sans-serif; font-size: 12.5px; color: var(--white); white-space: nowrap;
  }
</style>
</head>
<body>

<section class="card card-back" aria-label="Visitenkarte Rückseite">
  <span class="brand-mark"></span>
  <span class="brand-divider"></span>
  <p class="brand-name">Aigner Finanzberatung GmbH</p>
  <p class="brand-tagline">Finanzieren, Versichern, Vorsorgen</p>
  <p class="gisa">GISA Nr. 48270315 u. 51736048</p>
</section>

<section class="card card-front" aria-label="Visitenkarte Vorderseite">
  <span class="brand-mark"></span>
  <span class="brand-divider"></span>
  <p class="brand-name">Aigner Finanzberatung GmbH</p>
  <p class="brand-tagline">Finanzieren, Versichern, Vorsorgen</p>

  <div class="portrait" role="img" aria-label="Porträtfoto des Geschäftsführers im dunklen Sakko"></div>

  <h1 class="person-name">Bernhard Aigner</h1>
  <p class="person-role">Geschäftsführer</p>
  <p class="person-title">Staatl. Geprüfter Vermögensberater und Versicherungsmakler</p>
  <span class="name-rule"></span>

  <ul class="contact-list">
    <li><svg viewBox="0 0 24 24"><path d="M6.6 10.8a15.1 15.1 0 0 0 6.6 6.6l2.2-2.2a1 1 0 0 1 1-.25 11.4 11.4 0 0 0 3.6.57 1 1 0 0 1 1 1V20a1 1 0 0 1-1 1A17 17 0 0 1 3 4a1 1 0 0 1 1-1h3.5a1 1 0 0 1 1 1c0 1.25.2 2.45.57 3.57a1 1 0 0 1-.25 1z"/></svg>0664 521 8409</li>
    <li><svg viewBox="0 0 24 24"><path d="M2 5h20v14H2zM3.5 6.5v.4L12 12.5l8.5-5.6v-.4zM3.5 8.6v8.9h17V8.6L12 14.2z"/></svg>office@der-brandl.at</li>
    <li><svg viewBox="0 0 24 24"><path d="M12 2a10 10 0 1 0 0 20 10 10 0 0 0 0-20zm6.9 6h-3a15.6 15.6 0 0 0-1.4-3.6A8 8 0 0 1 18.9 8zM12 4c.8 1.2 1.5 2.5 1.9 4h-3.8c.4-1.5 1.1-2.8 1.9-4zM4.3 14a8 8 0 0 1 0-4h3.4a16 16 0 0 0 0 4zm.8 2h3a15.6 15.6 0 0 0 1.4 3.6A8 8 0 0 1 5.1 16zM8 8H5.1a8 8 0 0 1 4.4-3.6A15.6 15.6 0 0 0 8 8zm4 12c-.8-1.2-1.5-2.5-1.9-4h3.8c-.4 1.5-1.1 2.8-1.9 4zm2.3-6H9.7a14.6 14.6 0 0 1 0-4h4.6a14.6 14.6 0 0 1 0 4zm.2 5.6a15.6 15.6 0 0 0 1.4-3.6h3a8 8 0 0 1-4.4 3.6zm1.8-5.6a16 16 0 0 0 0-4h3.4a8 8 0 0 1 0 4z"/></svg>www.der-brandl.at</li>
  </ul>
  <p class="address">Leopold Hainz Gasse 14 2183 Melkstetten</p>

  <span class="partner-badge" role="img" aria-label="Partnersiegel"></span>

  <span class="band-gray"></span>
  <div class="band-blue">
    <svg width="253" height="32" viewBox="0 0 253 32" aria-hidden="true"><polygon points="14,0 253,0 253,32 0,32" fill="#0a56a0"/></svg>
    <p class="gisa">GISA Nr. 48270315 u. 51736048</p>
  </div>
</section>

</body>
</html>
```